TovarTunes poster

We need a poster to promote my live music show for hotels, Im playing for tourists in hotels in Palma de Mallorca, Spain, I would like to see the url of my web site in the poster www.tovartunes.es, in the web site you can see some of my music, thx

```html
<!DOCTYPE html>
<html lang="en">
<head>
<meta charset="UTF-8">
<title>TovarTunes – Live Music Poster</title>
<link href="https://fonts.googleapis.com/css2?family=Montserrat:wght@600;700&family=Pacifico&display=swap" rel="stylesheet">
<style>
  :root {
    --backdrop: #2a2a2a;
    --sage-light: #7fa390;
    --sage-mid: #5d8a72;
    --forest: #39594a;
    --ink: #111111;
    --paper: #ffffff;
    --sky: #a9c4e0;
    --sea: #3f6286;
    --hill: #55663f;
  }
  * { margin: 0; padding: 0; box-sizing: border-box; }
  html, body {
    width: 1200px; height: 1200px; overflow: hidden;
    background: var(--backdrop);
  }
  .poster {
    position: absolute;
    left: 290px; top: 171px;
    width: 627px; height: 880px;
    background: linear-gradient(180deg, var(--sage-light) 0%, var(--sage-mid) 60%, var(--forest) 100%);
    box-shadow: 6px 8px 18px rgba(0,0,0,0.5);
    overflow: hidden;
  }
  .poster__pattern {
    position: absolute; inset: 0;
    background: radial-gradient(ellipse at 30% 20%, rgba(255,255,255,0.08), transparent 60%);
  }
  .showcase {
    position: absolute;
    left: 0; top: 0;
    width: 627px; height: 720px;
  }
  .brand-name {
    position: absolute;
    left: 0; width: 627px; top: 118px;
    text-align: center;
    font-family: "Montserrat", sans-serif;
    font-weight: 700;
    font-size: 46px;
    color: var(--ink);
    letter-spacing: 1px;
  }
  .headline {
    position: absolute;
    left: 0; width: 627px; top: 680px;
    text-align: center;
    font-family: "Pacifico", cursive;
    font-size: 40px;
    color: var(--paper);
    line-height: 1.2;
  }
  .location {
    position: absolute;
    left: 60px; width: 504px; top: 745px;
    padding-bottom: 4px;
    border-bottom: 2px solid var(--paper);
    text-align: center;
    font-family: "Montserrat", sans-serif;
    font-weight: 700;
    font-size: 32px;
    color: var(--paper);
  }
  .website {
    position: absolute;
    left: 199px; top: 811px;
    width: 222px; height: 32px;
    border-radius: 16px;
    background: var(--paper);
    display: flex; align-items: center; justify-content: center;
    font-family: "Montserrat", sans-serif;
    font-weight: 600;
    font-size: 14px;
    letter-spacing: 1.5px;
    color: var(--ink);
  }
</style>
</head>
<body>
  <main class="poster">
    <div class="poster__pattern" role="img" aria-label="Faint pattern of musical notes and clefs"></div>

    <svg class="showcase" viewBox="0 0 627 720" aria-hidden="false">
      <defs>
        <linearGradient id="scene-fill" x1="0" y1="0" x2="0" y2="1">
          <stop offset="0" stop-color="#ffffff"/>
          <stop offset="0.3" stop-color="#ffffff"/>
          <stop offset="0.44" stop-color="#a9c4e0"/>
          <stop offset="0.52" stop-color="#5f7249"/>
          <stop offset="0.62" stop-color="#8c8a7a"/>
          <stop offset="0.7" stop-color="#4d6f94"/>
          <stop offset="0.85" stop-color="#2c2f3a"/>
          <stop offset="1" stop-color="#b8a06a"/>
        </linearGradient>
        <clipPath id="circle-clip">
          <circle cx="313" cy="357" r="294"/>
        </clipPath>
      </defs>
      <circle class="frame-outer" cx="313" cy="357" r="304" fill="#ffffff"/>
      <circle class="frame-inner" cx="313" cy="357" r="299" fill="#111111"/>
      <rect class="photo" role="img" aria-label="Guitarist playing on a hotel terrace above a harbour at dusk, hills and town behind"
            x="19" y="63" width="588" height="588" fill="url(#scene-fill)" clip-path="url(#circle-clip)"/>
    </svg>

    <div class="brand-name">TovarTunes</div>

    <p class="headline">Catch Me @</p>
    <p class="location">Palma de Mallorca, Spain</p>
    <div class="website">www.tovartunes.es</div>
  </main>
</body>
</html>
```